Product flyer with pricing

We manufacture iconic and luxury vending trailers. for our first trailer we need a flyer created to give to prospective clients with base pricing. I am uploading an example along with graphic files.

```html
<!DOCTYPE html>
<html lang="en">
<head>
<meta charset="utf-8">
<title>Meadow Cottage Mini – Product Flyer</title>
<link href="https://fonts.googleapis.com/css2?family=Arimo:wght@700&family=Lato:wght@400;700&display=swap" rel="stylesheet">
<style>
  :root {
    --green: #5fa548;
    --yellow: #f3b02e;
    --yellow-deep: #e29a1f;
    --ink: #1d1d1b;
    --text: #2b2b2b;
    --paper: #ffffff;
    --backdrop: #e6e6e6;
    --asphalt: #55585c;
  }
  * { box-sizing: border-box; margin: 0; padding: 0; }
  html, body { width: 1200px; height: 1200px; overflow: hidden; }
  body { background: var(--backdrop); font-family: "Lato", sans-serif; color: var(--text); position: relative; }

  .flyer {
    position: absolute; left: 171px; top: 48px;
    width: 858px; height: 1104px;
    background: var(--paper); overflow: hidden;
  }
  .header-art { position: absolute; left: 0; top: 0; width: 858px; height: 394px; display: block; }

  .brand-name {
    position: absolute; left: 560px; top: 332px; width: 250px;
    text-align: center; font-family: "Arimo", sans-serif; font-weight: 700;
    font-size: 22px; letter-spacing: 1px; color: var(--green);
  }

  .headline {
    position: absolute; left: 0; top: 418px; width: 858px; text-align: center;
    font-family: "Arimo", sans-serif; font-weight: 700; line-height: 1;
  }
  .headline .product { display: block; color: var(--green); font-size: 46px; }
  .headline .category { display: block; color: var(--yellow); font-size: 42px; margin-top: 12px; }

  .price-pill {
    position: absolute; left: 175px; top: 543px; width: 474px; height: 57px;
    border-radius: 29px;
    background: linear-gradient(90deg, var(--yellow-deep), var(--yellow));
    box-shadow: 0 10px 10px -6px rgba(0,0,0,0.25);
    color: #fff; font-family: "Arimo", sans-serif; font-weight: 700;
    font-size: 38px; line-height: 57px; text-align: center;
  }

  .section-title {
    position: absolute; font-family: "Arimo", sans-serif; font-weight: 700;
    font-size: 19px; line-height: 1; color: var(--ink);
  }
  .list { position: absolute; list-style: none; font-size: 13.5px; line-height: 16.5px; }
  .list li { position: relative; padding-left: 20px; margin-bottom: 8.5px; }
  .list.ticks li::before {
    content: ""; position: absolute; left: 3px; top: 3px; width: 10px; height: 10px;
    border: 1.2px solid var(--yellow); border-radius: 50%;
  }
  .list.ticks li::after {
    content: ""; position: absolute; left: 6.5px; top: 5.5px; width: 2.5px; height: 4px;
    border: solid var(--yellow); border-width: 0 1.2px 1.2px 0; transform: rotate(45deg);
  }
  .list.dots li::before {
    content: ""; position: absolute; left: 3px; top: 4.5px; width: 7px; height: 7px;
    border-radius: 50%; background: var(--green);
  }
  .price { color: var(--green); font-weight: 700; }

  .features-title { left: 45px; top: 637px; }
  .features { left: 45px; top: 670px; width: 330px; }
  .options-title { left: 461px; top: 639px; }
  .options { left: 461px; top: 672px; width: 350px; }
  .uses-title { left: 46px; top: 910px; }
  .uses { left: 46px; top: 945px; width: 470px; }

  .unit-photo {
    position: absolute; left: 553px; top: 841px; width: 305px; height: 263px;
    background: linear-gradient(180deg, #ffffff 0%, #f2f2f2 50%, #d9dadb 75%, #6d7073 88%, var(--asphalt) 100%);
  }
  .unit-ground {
    position: absolute; left: 422px; top: 1044px; width: 436px; height: 60px;
    background: linear-gradient(180deg, #7a7d80, var(--asphalt));
  }
  .footer-band {
    position: absolute; left: 0; top: 1051px; width: 422px; height: 53px;
    background: var(--green); display: flex; align-items: center; padding-left: 198px;
    padding-left: 65px;
  }
  .footer-band svg { width: 21px; height: 21px; margin-right: 15px; }
  .footer-band .web { color: #fff; font-family: "Arimo", sans-serif; font-weight: 700; font-size: 15px; letter-spacing: 1.5px; }
</style>
</head>
<body>
  <main class="flyer">
    <svg class="header-art" viewBox="0 0 1384 636" preserveAspectRatio="none">
      <defs>
        <linearGradient id="photoTone" x1="0" y1="0" x2="0" y2="1">
          <stop offset="0" stop-color="#8fa9c9"/>
          <stop offset="0.45" stop-color="#7a6f5e"/>
          <stop offset="0.7" stop-color="#e9ecef"/>
          <stop offset="1" stop-color="#4d4f52"/>
        </linearGradient>
      </defs>
      <polygon role="img" aria-label="Photo of the white board-and-batten vending house on its trailer with the serving window being opened" points="0,0 716,0 906,306 780,554 0,554" fill="url(#photoTone)"/>
      <polygon points="716,0 1086,0 906,306" fill="var(--yellow)"/>
      <polygon points="1086,0 1384,0 1384,108 1116,108 811,636 0,636 0,554 780,554 906,306" fill="var(--green)"/>
    </svg>

    <div class="brand-name">SUNVALE CABINS</div>

    <h1 class="headline">
      <span class="product">THE“MEADOW COTTAGE MINI”</span>
      <span class="category">LUXURY, MOBILE VENDING HOUSE</span>
    </h1>

    <div class="price-pill">BASE PRICE: $45,000</div>

    <h2 class="section-title features-title">BASE UNIT FEATURES</h2>
    <ul class="list ticks features">
      <li>Trailer features tandem wheels w/ brakes</li>
      <li>Steel frame construction for fire retardation safety and weight reduction.</li>
      <li>100% off grid with solar and lithium battery system allowing the trailer to be used in places not accessible by traditional trailers.</li>
      <li>80 gallon water supply tank</li>
      <li>100 gallon waste water tank</li>
      <li>Cupboards, cabinets &amp; four stainless steel sinks.</li>
      <li>60” Gas shock serving window</li>
    </ul>

    <h2 class="section-title options-title">AVAILABLE OPTIONS</h2>
    <ul class="list dots options">
      <li>HVAC - Coolwave Mini Split - <span class="price">$1,800</span></li>
      <li>Cooler / Glass front Commercial refrigerator - <span class="price">$1,600</span></li>
      <li>Upper loft storage area - <span class="price">$1,200</span></li>
      <li>Signage and graphics - <span class="price">$2,000 - $5,000</span> depend on complexity</li>
      <li>Ice machine - <span class="price">$1,100</span></li>
      <li>Other custom items available on request.</li>
    </ul>

    <h2 class="section-title uses-title">USE CASES</h2>
    <ul class="list ticks uses">
      <li>Food: Lemonade, Coffee, pizza, cookies, doughnuts, barbecue and more!</li>
      <li>Retail: Clothing, watches, jewelry, flowers and more!</li>
      <li>Corporate: Product info, demonstration, information, brand awareness.</li>
      <li>Fundraisers: Girls/boy sports, non profits, etc.</li>
    </ul>

    <div class="unit-ground" aria-hidden="true"></div>
    <div class="unit-photo" role="img" aria-label="Photo of the vending house from the gable end with front door, parked on asphalt"></div>

    <footer class="footer-band">
      <svg viewBox="0 0 24 24" fill="none" stroke="#fff" stroke-width="1.5" aria-hidden="true">
        <circle cx="12" cy="12" r="10"/>
        <ellipse cx="12" cy="12" rx="4.5" ry="10"/>
        <line x1="2" y1="12" x2="22" y2="12"/>
        <path d="M4 6.5h16M4 17.5h16"/>
      </svg>
      <span class="web">www.sunvalecabins.com</span>
    </footer>
  </main>
</body>
</html>
```